Modern Skincare Product Label with Logo (please look at uploaded pics)

We need a product label and logo for a skincare line. We are looking for a design for 1 tall skinny container and 1 layout that works for short wide jar containers.

Our containers are white and silver plastic.

The dimensions of the label for the tall skinny container is about 3 1/2 in wide by 3 6/8 inches tall. That is what we want designed for.

Our product line is called Meridel Skincare. We are looking for more modern design. Please try a design with meridel in bold and going vertical down the product as well as looking at the uploaded pics we posted and getting creative with them.

We are attaching product inspirations and also our blank containers.

Target Market(s)

We are looking for something gender neutral (but slightly leaning more toward targeting women).

Industry/Entity Type

Skin Care Product

Font styles to use
Sans Serif

Colors

Designer to choose colors to be used in the design.

Requirements
Must have
• We prefer a logo and packaging that is modern, simple. The background must be white. We will have about 6 different skincare categories (categories like, acne, anti-aging, normal skin, etc). We'd like that splash of color to indicate which product category it is. accent colors: bright turquoise or Orange. can have grey and black letters. modern.
• Must have a place for a barcode, ingredients list, and any other things that we're supposed to have on a label.
Nice to have
• I'm attaching pictures we like. We are targeting more high end younger crowd.
Should not have
• No clip art or typical "spa" images or outlines of a face incorporated into the logo (we think that's super cheesy). modern and sleek design. I don't like the MS in the logo.

```html
<!DOCTYPE html>
<html lang="en">
<head>
<meta charset="utf-8">
<title>Meridel Skincare – Acne Label</title>
<link rel="stylesheet" href="https://fonts.googleapis.com/css2?family=Lato:wght@400;700&family=Oswald:wght@400;500&family=Questrial&display=swap">
<style>
  :root {
    --page: #ffffff;
    --ink: #1a1a1a;
    --orange: #f7931e;
    --orange-deep: #f39a1c;
    --orange-soft: #fbb03b;
    --cream: #f9e3bd;
    --label-top: #ffffff;
    --label-mid: #fbeccb;
    --grey-text: #4d4d4d;
  }
  * { margin: 0; padding: 0; box-sizing: border-box; }
  html, body {
    width: 1200px; height: 1200px; overflow: hidden;
    background: var(--page);
  }
  .canvas { position: relative; width: 1200px; height: 1200px; }

  .label {
    position: absolute; left: 390px; top: 40px;
    width: 420px; height: 1116px;
    background: linear-gradient(180deg,
      var(--label-top) 0%, var(--label-top) 18%,
      var(--label-mid) 40%, var(--orange-soft) 78%, var(--orange-deep) 100%);
    overflow: hidden;
  }
  .label-texture {
    position: absolute; inset: 0;
    background: linear-gradient(160deg, rgba(255,255,255,0) 40%, rgba(255,255,255,0.25) 55%, rgba(255,255,255,0) 70%);
  }

  .brand {
    position: absolute; left: 0; right: 0; top: 58px;
    display: flex; flex-direction: column; align-items: center;
  }
  .brand-mark {
    width: 120px; height: 120px;
    border: 5px solid var(--ink);
    margin-bottom: 44px;
  }
  .brand-name {
    font-family: "Lato", sans-serif; font-weight: 700;
    color: var(--ink); font-size: 30px; line-height: 1.1;
    text-align: center; letter-spacing: 1px;
  }

  .category {
    position: absolute; left: 17px; width: 382px; top: 558px;
    height: 124px;
    background: var(--orange);
    border: 3px solid var(--ink);
    display: flex; align-items: center; justify-content: center;
  }
  .category-name {
    font-family: "Questrial", sans-serif; color: var(--ink);
    font-size: 104px; line-height: 1; letter-spacing: 8px;
    margin-top: -10px;
  }

  .info {
    position: absolute; left: 25px; width: 368px; top: 682px;
    height: 192px;
    background: var(--cream);
    border: 3px solid var(--ink); border-top: none;
    display: flex;
  }
  .info-strength {
    width: 72px; border-right: 3px solid var(--ink);
    display: flex; align-items: center; justify-content: center;
  }
  .info-strength span {
    font-family: "Oswald", sans-serif; font-weight: 500;
    font-size: 19px; color: var(--ink); white-space: nowrap;
    transform: rotate(-90deg); letter-spacing: 0.5px;
  }
  .info-claim {
    flex: 1; padding: 34px 20px 0 18px;
    font-family: "Lato", sans-serif; font-size: 20px;
    line-height: 1.35; color: var(--ink); text-align: justify;
  }

  .volume {
    position: absolute; left: 0; right: 0; bottom: 38px;
    text-align: center;
    font-family: "Oswald", sans-serif; font-size: 22px;
    color: var(--grey-text);
  }
</style>
</head>
<body>
<main class="canvas">
  <section class="label">
    <div class="label-texture"></div>

    <header class="brand">
      <div class="brand-mark"></div>
      <p class="brand-name">Meridel<br>Skincare</p>
    </header>

    <div class="category">
      <h1 class="category-name">acne</h1>
    </div>

    <div class="info">
      <div class="info-strength"><span>A 5% LIQUID BENZOYL</span></div>
      <p class="info-claim">Penetrate pores to clear existing acne blemishes and Prevent the occurrence of future Breakouts.</p>
    </div>

    <p class="volume">30 ML</p>
  </section>
</main>
</body>
</html>
```